Successfully Managing through a Hurricane Training Event

This learning event is specifically for Birch Supply retailers/stores located outside of the US who are seeking guidance and help with how to plan, prepare, manage there business during Hurricane/Tropical Storm season.

----------------------------------------------
Event Title: Successfully Managing Through Hurricane Season

Event Description: Hurricanes and severe tropical storms are some of the most devastating, and costly, natural disasters known to humans. In fact, historically, 40% of small businesses impacted by a natural disaster do not reopen. If your business is vulnerable to these potential catastrophic events, it is important to develop an effective preparedness and mitigation plan, and take prompt action. Doing so will not only increase the safety of your store associates and customers, but it will help you remain in business after a hurricane strikes, improving your community’s ability to recover. This session focuses on:

o In-store preparation functions
o Implementing business continuity operating procedures for protecting and maintaining your business
o Sustaining the capability to provide products to customers
o Building a hurricane-ready optimized assortment of in-demand products, including special merchandising opportunities
o Deploying effective inventory management and system strategies for staying in stock
o Knowing your available contacts and rules of engagement
o Preserving a competitive advantage and reputation
o Optimizing the means by which you leverage your freight forwarding facility

Event is hosted by: Birch Worldwide Partners www.birchworldpartnersco.example

Logistical Details:
• Length: 1 hour
• Date: Friday, August 17, 2018
• Time: 1:00 – 2:00 p.m.

To Register for this Event, Go To: https://www.tolvenork.example/birch18/fall/

Pricing: $ 25 per participant
*Charged to Invoice post-show

Questions? For more information, contact Martin Oakes
+1 555-017-2846
moakes@birchsupply.example

Target Market(s)

Birch Supply International Stores

Industry/Entity Type

Retail

Font styles to use
Serif

Requirements
Must have
• See Word File Attachment
• Use Birch Supply red and black logo colors.
• 1 -Sided brochure
Nice to have
Should not have
• N/A

```html
<!DOCTYPE html>
<html lang="en">
<head>
<meta charset="utf-8">
<title>Successfully Managing Through Hurricane Season</title>
<link rel="stylesheet" href="https://fonts.googleapis.com/css2?family=Open+Sans:wght@400;600;700;800&display=swap">
<style>
  :root {
    --red: #c8102e;
    --red-dark: #8e0b1f;
    --ink: #1e1e1e;
    --charcoal: #2b2b2b;
    --grey: #5a5a5a;
    --paper: #ffffff;
  }
  * { box-sizing: border-box; margin: 0; padding: 0; }
  html, body { width: 707px; height: 1200px; overflow: hidden; background: var(--paper); }
  body { font-family: "Open Sans", Arial, sans-serif; color: var(--ink); position: relative; }

  .header { position: absolute; top: 0; left: 0; width: 707px; height: 110px; }
  .header-band { position: absolute; top: 0; left: 0; }
  .brand { position: absolute; top: 28px; left: 30px; display: flex; align-items: center; gap: 10px; }
  .brand-mark { width: 34px; height: 34px; border-radius: 50%; background: var(--red); }
  .brand-name { font-weight: 800; font-size: 19px; color: var(--red); text-transform: uppercase; letter-spacing: .5px; }

  .hero { position: absolute; top: 110px; left: 0; width: 707px; height: 360px;
    background: linear-gradient(180deg, #3b4147 0%, #5d666c 45%, #3f6b6c 72%, #2c3b3e 100%); }
  .hero-swoosh { position: absolute; left: 0; top: 400px; }

  .title-band { position: absolute; top: 470px; left: 0; width: 707px; height: 52px; background: var(--red);
    display: flex; align-items: center; padding-left: 30px; }
  .title { color: #fff; font-weight: 800; font-size: 21px; text-transform: uppercase; letter-spacing: .3px; }
  .event-date { position: absolute; top: 532px; right: 30px; font-weight: 800; font-size: 22px; color: var(--red); }

  .description { position: absolute; top: 570px; left: 30px; width: 647px; font-size: 10.5px; line-height: 1.5; color: var(--grey); }
  .description strong { color: var(--ink); }

  .focus { position: absolute; top: 660px; left: 0; width: 707px; height: 262px; background: var(--red); padding: 14px 30px; }
  .focus-heading { color: #fff; font-weight: 800; font-size: 26px; line-height: 36px; margin-bottom: 12px; }
  .focus-list { list-style: none; display: grid; grid-template-columns: 1fr 1fr; grid-auto-rows: 40px; gap: 8px 14px; }
  .focus-item { background: var(--paper); border-radius: 3px; display: flex; align-items: center; gap: 8px; padding: 0 10px; font-size: 9.5px; line-height: 1.25; color: var(--ink); }
  .focus-item svg { flex: none; }

  .host-band { position: absolute; top: 922px; left: 0; width: 707px; height: 34px; background: var(--charcoal);
    color: #fff; font-size: 13px; display: flex; align-items: center; padding-left: 30px; gap: 6px; }
  .host-band b { font-weight: 700; }
  .host-band .host-url { color: #f2a3ae; }

  .logistics { position: absolute; top: 972px; left: 30px; width: 320px; }
  .logistics-heading { font-weight: 800; font-size: 22px; color: var(--red); text-transform: uppercase; margin-bottom: 8px; }
  .logistics-row { font-size: 16px; line-height: 1.65; }
  .logistics-row b { font-weight: 700; }

  .register { position: absolute; top: 972px; left: 380px; width: 297px; }
  .register-lead { font-size: 15px; font-weight: 600; }
  .register-url { font-size: 11px; font-weight: 700; color: var(--red); margin-top: 6px; word-break: break-all; }
  .pricing { margin-top: 16px; font-size: 28px; font-weight: 800; color: var(--ink); line-height: 1.1; }
  .pricing .amount { color: var(--red); }
  .pricing-note { font-size: 11px; color: var(--grey); font-style: italic; margin-top: 4px; }

  .footer { position: absolute; top: 1140px; left: 0; width: 707px; height: 60px; background: var(--charcoal);
    display: flex; align-items: center; justify-content: space-between; padding: 0 30px; color: #fff; font-size: 12px; }
  .footer-contact b { font-weight: 700; }
  .footer-phone { color: #fff; font-weight: 700; font-size: 14px; display: flex; align-items: center; gap: 6px; }
  .footer-email { font-weight: 600; }
</style>
</head>
<body>
  <header class="header">
    <svg class="header-band" width="707" height="110" viewBox="0 0 707 110" aria-hidden="true">
      <path d="M330 0 H707 V70 C600 40 470 30 330 0 Z" fill="var(--red)"/>
      <path d="M400 0 H707 V40 C620 22 510 14 400 0 Z" fill="var(--red-dark)"/>
    </svg>
    <div class="brand">
      <span class="brand-mark"></span>
      <span class="brand-name">Birch Worldwide Partners</span>
    </div>
  </header>

  <div class="hero" role="img" aria-label="Photograph of palm trees bending over a stormy sea under dark hurricane clouds"></div>
  <svg class="hero-swoosh" width="707" height="70" viewBox="0 0 707 70" aria-hidden="true">
    <path d="M0 10 C150 40 300 55 460 70 H0 Z" fill="var(--red)"/>
  </svg>

  <div class="title-band">
    <h1 class="title">Successfully Managing Through Hurricane Season</h1>
  </div>
  <p class="event-date">Date: 20 June 2018</p>

  <p class="description"><strong>Event Description:</strong> Hurricanes and severe tropical storms are some of the most devastating, and costly, natural disasters known to humans. In fact, historically, 40% of small businesses impacted by a natural disaster do not reopen. If your business is vulnerable to these potential catastrophic events, it is important to develop an effective preparedness and mitigation plan, and take prompt action. Doing so will not only increase the safety of your store associates and customers, but it will help you remain in business after a hurricane strikes, improving your community’s ability to recover.</p>

  <section class="focus">
    <h2 class="focus-heading">This session focuses on:</h2>
    <ul class="focus-list">
      <li class="focus-item"><svg width="12" height="12" viewBox="0 0 12 12"><circle cx="6" cy="6" r="6" fill="var(--red)"/></svg>In-store preparation functions</li>
      <li class="focus-item"><svg width="12" height="12" viewBox="0 0 12 12"><circle cx="6" cy="6" r="6" fill="var(--red)"/></svg>Deploying effective inventory management and system strategies for staying in stock</li>
      <li class="focus-item"><svg width="12" height="12" viewBox="0 0 12 12"><circle cx="6" cy="6" r="6" fill="var(--red)"/></svg>Implementing business continuity operating procedures for protecting and maintaining your business</li>
      <li class="focus-item"><svg width="12" height="12" viewBox="0 0 12 12"><circle cx="6" cy="6" r="6" fill="var(--red)"/></svg>Knowing your available contacts and rules of engagement</li>
      <li class="focus-item"><svg width="12" height="12" viewBox="0 0 12 12"><circle cx="6" cy="6" r="6" fill="var(--red)"/></svg>Sustaining the capability to provide products to customers</li>
      <li class="focus-item"><svg width="12" height="12" viewBox="0 0 12 12"><circle cx="6" cy="6" r="6" fill="var(--red)"/></svg>Preserving a competitive advantage and reputation</li>
      <li class="focus-item"><svg width="12" height="12" viewBox="0 0 12 12"><circle cx="6" cy="6" r="6" fill="var(--red)"/></svg>Building a hurricane-ready optimized assortment of in-demand products, including special merchandising opportunities</li>
      <li class="focus-item"><svg width="12" height="12" viewBox="0 0 12 12"><circle cx="6" cy="6" r="6" fill="var(--red)"/></svg>Optimizing the means by which you leverage your freight forwarding facility</li>
    </ul>
  </section>

  <div class="host-band">Event is hosted by: <b>Birch Worldwide Partners</b> <span class="host-url">www.birchworldpartnersco.example</span></div>

  <section class="logistics">
    <h2 class="logistics-heading">Logistical Details:</h2>
    <p class="logistics-row"><b>Length:</b> 1 hour</p>
    <p class="logistics-row"><b>Date:</b> Friday, August 17, 2018</p>
    <p class="logistics-row"><b>Time:</b> 1:00 – 2:00 p.m.</p>
  </section>

  <section class="register">
    <p class="register-lead">To Register for this Event, Go To:</p>
    <p class="register-url">https://www.tolvenork.example/birch18/fall/</p>
    <p class="pricing">Pricing: <span class="amount">$25</span> per participant</p>
    <p class="pricing-note">*Charged to Invoice post-show</p>
  </section>

  <footer class="footer">
    <span class="footer-contact">Questions? For more information, contact <b>Martin Oakes</b></span>
    <span class="footer-phone"><svg width="14" height="14" viewBox="0 0 24 24"><path d="M6.6 10.8a15 15 0 0 0 6.6 6.6l2.2-2.2a1 1 0 0 1 1-.25 11.4 11.4 0 0 0 3.6.6 1 1 0 0 1 1 1V20a1 1 0 0 1-1 1A17 17 0 0 1 3 4a1 1 0 0 1 1-1h3.5a1 1 0 0 1 1 1c0 1.25.2 2.45.6 3.6a1 1 0 0 1-.25 1z" fill="#fff"/></svg>+1 555-017-2846</span>
    <span class="footer-email">moakes@birchsupply.example</span>
  </footer>
</body>
</html>
```